Quillmere Surgical Clinic ,Perth- Australia

We need a letterhead for our surgical clinic , it needs to highlight all the relevant contact details and practice locations. needs to be eye catching, but remain professional.all the logos attached
clear contact details as follows

Surgeon name : Mr Tevin Oskard
Phone : 1300 482 917 - 0417 296 481
Fax : 08- 7524 3968
email : tevin@parvellaclinicgroup.com.au
www.parvellaclinicgroup.com.au

Consults from
1- Haldane Medical Centre - Level 3 - Suite 42.
9 Cotterill Vance Parade
Murdoch WA 6157

2- KBRT Mandurah Suites
54 Pellingham Road Mandurah 6214

Operates at :
Our Lady of Peace Murdoch Hospital
Doreen Whitcombe Hospital
Tarn Health Campus
Rookwell Hospital
Ravenfield Hopital
Our Lady of Peace Subiaco

Target Market(s)

General Practitioners (Family doctors)

Industry/Entity Type

Medical

Requirements
Must have
• all the logos attached
• clear contact details as follows
• Surgeon name : Mr Tevin Oskard
• Phone : 1300 482 917 - 0417 296 481
• Fax : 08- 7524 3968
• email : tevin@parvellaclinicgroup.com.au
• www.parvellaclinicgroup.com.au
• Consults from
• 1- Haldane Medical Centre - Level 3 - Suite 42.
• 9 Cotterill Vance Parade
• Murdoch WA 6157
• 2- KBRT Mandurah Suites
• 54 Pellingham Road Mandurah 6214
• Operates at :
• Our Lady of Peace Murdoch Hospital
• Doreen Whitcombe Hospital
• Tarn Health Campus
• Rookwell Hospital
• Ravenfield Hopital
• Our Lady of Peace Subiaco
Nice to have
• a surgical theme in the design , but remain professional
Should not have
• big chunky designs
• no photographs or diagrams of objects (ECG, or stethoscope ..ect)

```html
<!DOCTYPE html>
<html lang="en">
<head>
<meta charset="utf-8">
<title>Quillmere Surgical Clinic – Letterhead</title>
<link rel="stylesheet" href="https://fonts.googleapis.com/css2?family=Arimo:wght@400;700&family=Open+Sans:wght@400;600&display=swap">
<style>
  :root {
    --brand-blue: #1b5c94;
    --brand-red: #b1261d;
    --ring-blue: #a9cfe6;
    --badge-navy: #2b3d8f;
    --badge-grey: #9aa3ad;
    --badge-teal: #8fd0dc;
    --badge-pink: #d8558e;
    --paper: #ffffff;
    --backdrop: #e6e6e8;
  }
  * { margin: 0; padding: 0; box-sizing: border-box; }
  html, body { width: 1200px; height: 991px; overflow: hidden; background: var(--backdrop); }
  .letterhead {
    position: absolute; left: 223px; top: 10px;
    width: 754px; height: 971px; background: var(--paper);
    border-top: 1px solid #7fc6d8;
    box-shadow: 0 1px 4px rgba(0,0,0,.15);
    font-family: "Open Sans", sans-serif; color: var(--brand-blue);
  }
  .abs { position: absolute; white-space: nowrap; }
  .clinic-name {
    left: 178px; top: 25px; width: 150px; text-align: center;
    font-family: "Arimo", sans-serif; font-weight: 400;
    font-size: 17px; line-height: 22px; letter-spacing: 2.2px; color: var(--brand-blue);
  }
  .clinic-mark { left: 332px; top: 11px; }
  .surgeon-name {
    left: 432px; top: 50px; font-family: "Arimo", sans-serif;
    font-size: 17px; color: var(--brand-blue);
  }
  .specialty {
    left: 0; width: 754px; top: 104px; text-align: center;
    font-family: "Arimo", sans-serif; font-size: 11.5px; color: var(--brand-blue);
  }
  .contact-row { top: 126px; left: 0; width: 754px; font-size: 8.6px; }
  .contact-item { position: absolute; display: flex; align-items: center; gap: 4px; }
  .contact-item svg { flex: none; }
  .rule { left: 70px; width: 627px; height: 2px; background: var(--brand-red); }
  .rule-top { top: 141px; }
  .rule-bottom { top: 203px; }
  .section-label { font-size: 10.5px; font-weight: 600; color: var(--brand-red); }
  .address-lines { font-size: 8.4px; line-height: 11.5px; }
  .address-lines .sub-label { color: var(--brand-red); }
  .consults-label { left: 75px; top: 151px; }
  .consults-text { left: 155px; top: 153px; }
  .operates-label { left: 353px; top: 152px; }
  .operates-text { left: 426px; top: 154px; }
  .affiliations { left: 68px; top: 893px; width: 630px; height: 64px; }
</style>
</head>
<body>
  <main class="letterhead">
    <header>
      <div class="abs clinic-name">QUILLMERE<br>SURGICAL<br>CLINIC</div>
      <svg class="abs clinic-mark" width="90" height="90" viewBox="0 0 90 90" aria-hidden="true">
        <circle cx="45" cy="45" r="42" fill="none" stroke="var(--ring-blue)" stroke-width="4"/>
      </svg>
      <div class="abs surgeon-name">MR TEVIN OSKARD</div>
      <div class="abs specialty">ENDOCRINE , BREAST AND GENERAL SURGEON</div>

      <div class="abs contact-row">
        <div class="contact-item" style="left:128px">
          <svg width="9" height="9" viewBox="0 0 10 10"><rect width="10" height="10" rx="1.5" fill="var(--brand-red)"/><path d="M3 2.2c-.5.4-.6 1.3 0 2.6.7 1.4 1.7 2.6 3 3.1.6.2 1 0 1.3-.4l-1.1-1-.7.4C4.8 6.4 4 5.4 3.7 4.6l.6-.5-.8-1.6z" fill="#fff"/></svg>
          <span>1300 482 917 - 0417 296 481</span>
        </div>
        <div class="contact-item" style="left:274px">
          <svg width="10" height="9" viewBox="0 0 10 9"><rect x="2.5" y="0" width="5" height="3" fill="var(--brand-red)"/><rect x="0" y="3" width="10" height="4" rx="1" fill="var(--brand-red)"/><rect x="2.5" y="6" width="5" height="3" fill="#fff" stroke="var(--brand-red)" stroke-width="1"/></svg>
          <span>08- 7524 3968</span>
        </div>
        <div class="contact-item" style="left:371px"><span>eReferral ID: quillsurg</span></div>
        <div class="contact-item" style="left:481px">
          <svg width="10" height="10" viewBox="0 0 10 10" fill="none" stroke="var(--brand-red)" stroke-width=".9"><circle cx="5" cy="5" r="4.3"/><ellipse cx="5" cy="5" rx="1.9" ry="4.3"/><path d="M.8 5h8.4M1.6 2.8h6.8M1.6 7.2h6.8"/></svg>
          <span>www.parvellaclinicgroup.com.au</span>
        </div>
      </div>

      <div class="abs rule rule-top"></div>

      <div class="abs section-label consults-label">Consults From</div>
      <div class="abs address-lines consults-text">
        Haldane Medical Centre Level 3 - Suite 42<br>
        9 Cotterill Vance Parade Murdoch WA 6157<br>
        <span class="sub-label">&nbsp;KBRT Mandurah Suites</span><br>
        &nbsp;54 Pellingham Road Mandurah 6214
      </div>

      <div class="abs section-label operates-label">Operates at :</div>
      <div class="abs address-lines operates-text">
        Our Lady of Peace Murdoch Hospital | Doreen Whitcombe Hospital<br>
        Tarn Health Campus | Rookwell Hospital Ravenfield Hopital<br>
        Our Lady of Peace Subiaco
      </div>

      <div class="abs rule rule-bottom"></div>
    </header>

    <footer>
      <svg class="abs affiliations" viewBox="0 0 630 64" aria-label="Professional affiliation badges">
        <circle cx="29" cy="32" r="28" fill="var(--badge-navy)"/>
        <rect x="66" y="14" width="130" height="38" rx="3" fill="var(--badge-grey)" opacity=".55"/>
        <rect x="208" y="20" width="126" height="26" rx="13" fill="var(--badge-grey)" opacity=".45"/>
        <rect x="347" y="12" width="50" height="40" rx="4" fill="#3a3a3a" opacity=".8"/>
        <rect x="411" y="0" width="100" height="28" rx="3" fill="var(--badge-pink)" opacity=".35"/>
        <rect x="411" y="34" width="100" height="28" rx="3" fill="var(--badge-navy)" opacity=".35"/>
        <rect x="527" y="4" width="62" height="56" rx="3" fill="var(--badge-teal)" opacity=".55"/>
        <rect x="600" y="4" width="30" height="56" fill="#2b5d9b"/>
      </svg>
    </footer>
  </main>
</body>
</html>
```